Large multi-office optometry business opening a Dry Eye Spa and needs sign.

Business name/sign info: Brenwick Dry Eye Institute, (555) 362-4817
Backlit pole sign at office entrance on a very busy street
Sign dimensions: 53" tall x 136.5" wide
State of the art Dry Eye Spa for treatment of all forms of dry eye and ocular surface disease. Also, have aesthetics treatments (IPL, Low Level Light Treatment, etc.)

Target Market(s)

People who are suffering from: dryness, burning, foreign body sensation, itching, fluctuating vision, tired eyes, etc.

Industry/Entity Type

Optometry and aesthetics

Colors
0054AA
0677BA
7BADD7
CADEEF
E8F1F8

Requirements
Must have
• Business name, phone number, subliminal message of relief in a glance or short look.
Nice to have
• Cool, relief, soothing sense.
Should not have
• Too much information or too busy.

```html
<!DOCTYPE html>
<html lang="en">
<head>
<meta charset="utf-8">
<title>Brenwick Dry Eye Institute — Pole Sign</title>
<link rel="stylesheet" href="https://fonts.googleapis.com/css2?family=Montserrat:wght@600&display=swap">
<style>
  :root {
    --deep-blue: #0054AA;
    --mid-blue: #0677BA;
    --sky-blue: #7BADD7;
    --pale-blue: #CADEEF;
    --mist: #E8F1F8;
    --frame: #2b3a47;
    --backdrop: #f4f6f8;
  }
  * { margin: 0; padding: 0; box-sizing: border-box; }
  html, body {
    width: 1200px;
    height: 1200px;
    overflow: hidden;
    background: var(--backdrop);
  }
  .canvas {
    position: relative;
    width: 1200px;
    height: 1200px;
    display: flex;
    align-items: center;
    justify-content: center;
  }
  .sign-face {
    position: relative;
    width: 1100px;
    height: 850px;
    border: 14px solid var(--frame);
    background: radial-gradient(ellipse at 55% 30%, #ffffff 0%, var(--mist) 35%, var(--pale-blue) 70%, var(--sky-blue) 100%);
    overflow: hidden;
    font-family: "Montserrat", sans-serif;
    font-weight: 600;
    color: var(--deep-blue);
  }
  .wave-band {
    position: absolute;
    left: 0;
    right: 0;
    top: 500px;
    height: 336px;
    background: linear-gradient(180deg, rgba(202,222,239,0) 0%, rgba(123,173,215,0.55) 30%, rgba(6,119,186,0.45) 60%, rgba(123,173,215,0.6) 100%);
  }
  .brand {
    position: absolute;
    left: 70px;
    top: 150px;
    display: flex;
    align-items: center;
    gap: 50px;
  }
  .brand-dot {
    width: 200px;
    height: 200px;
    border-radius: 50%;
    background: var(--deep-blue);
    flex: none;
  }
  .brand-name {
    display: flex;
    flex-direction: column;
    line-height: 1;
    text-transform: uppercase;
  }
  .brand-name .line-first { font-size: 96px; letter-spacing: 2px; }
  .brand-name .line-main { font-size: 128px; margin-top: 10px; }
  .brand-name .line-last { font-size: 54px; letter-spacing: 18px; margin-top: 14px; padding-left: 30px; }
  .phone {
    position: absolute;
    left: 0;
    right: 0;
    top: 680px;
    text-align: center;
    font-size: 92px;
    letter-spacing: 2px;
    padding-right: 120px;
  }
</style>
</head>
<body>
  <main class="canvas">
    <section class="sign-face">
      <div class="wave-band" role="img" aria-label="Soft flowing blue water waves across the lower part of the sign"></div>
      <div class="brand">
        <div class="brand-dot"></div>
        <h1 class="brand-name">
          <span class="line-first">Brenwick</span>
          <span class="line-main">Dry Eye</span>
          <span class="line-last">Institute</span>
        </h1>
      </div>
      <p class="phone">(555) 362-4817</p>
    </section>
  </main>
</body>
</html>
```